Executive Coaching and Spiritual Development Company needs a business card design.

We need a business card design for our company. We already have a logo that was created through Loomquarry that we will submit and would like to see this work on black, blue and white backgrounds. Our personal information should be included as well. The design should communicate trust, spirituality, support and partnership.

Industry/Entity Type

Business

Colors
0255a3
33a6d7
ffffff
000000
474747

Requirements
Nice to have
• The colors offered here are just ideas--we are open to other suggestions, too.

```html
<!DOCTYPE html>
<html lang="en">
<head>
<meta charset="utf-8">
<title>Innerharbor Business Card</title>
<link rel="stylesheet" href="https://fonts.googleapis.com/css2?family=Roboto+Slab:wght@500&family=Open+Sans:wght@400;600&display=swap">
<style>
  :root {
    --page-bg: #e9e7e4;
    --card-dark-top: #123a48;
    --card-dark-bottom: #041820;
    --card-light: #ffffff;
    --ink-light: #ffffff;
    --ink-dark: #2f3a40;
    --ring-faint: #c9d2d6;
    --ring-bright: #f2f2f2;
  }
  * { margin: 0; padding: 0; box-sizing: border-box; }
  html, body {
    width: 1200px; height: 900px; overflow: hidden;
    background: var(--page-bg);
  }
  .canvas {
    position: relative; width: 1200px; height: 900px;
  }
  .card {
    position: absolute; top: 302px;
    width: 520px; height: 297px;
    border-radius: 4px;
    overflow: hidden;
    box-shadow: 0 10px 24px rgba(0,0,0,0.22);
  }
  .card-front {
    left: 50px;
    background: linear-gradient(160deg, var(--card-dark-top) 0%, var(--card-dark-bottom) 75%);
  }
  .brand-lockup {
    position: absolute; left: 70px; top: 108px;
    display: flex; align-items: center; gap: 16px;
  }
  .brand-circle {
    width: 80px; height: 80px; border-radius: 50%;
    border: 3px solid var(--ring-bright);
  }
  .brand-name {
    font-family: "Roboto Slab", serif;
    font-weight: 500;
    font-size: 50px;
    color: var(--ink-light);
    letter-spacing: 0.5px;
  }
  .card-back {
    left: 630px;
    background: var(--card-light);
  }
  .card-back svg.back-shapes {
    position: absolute; inset: 0;
  }
  .holder {
    position: absolute; right: 26px; top: 18px;
    text-align: right;
    color: var(--ink-light);
    font-family: "Open Sans", sans-serif;
  }
  .holder-name { font-size: 22px; font-weight: 400; letter-spacing: 0.5px; line-height: 1.1; }
  .holder-role { font-size: 16px; line-height: 1.3; }
  .contact {
    position: absolute; left: 300px; top: 128px;
    font-family: "Open Sans", sans-serif;
    font-size: 14px; color: var(--ink-dark);
    list-style: none; line-height: 1.45;
  }
  .contact li { display: flex; align-items: flex-start; gap: 6px; }
  .contact .address { margin-top: 12px; }
  .contact svg { width: 11px; height: 11px; margin-top: 5px; flex: none; fill: var(--ink-dark); }
</style>
</head>
<body>
<main class="canvas">
  <section class="card card-front">
    <div class="brand-lockup">
      <span class="brand-circle"></span>
      <span class="brand-name">Innerharbor</span>
    </div>
  </section>

  <section class="card card-back">
    <svg class="back-shapes" width="520" height="297" viewBox="0 0 520 297">
      <defs>
        <linearGradient id="band" x1="0" y1="0" x2="1" y2="1">
          <stop offset="0" stop-color="#1d4a59"/>
          <stop offset="1" stop-color="#05202a"/>
        </linearGradient>
      </defs>
      <path d="M150 0 L520 0 L520 150 C470 60 330 18 150 0 Z" fill="url(#band)"/>
      <circle cx="150" cy="215" r="135" fill="none" stroke="var(--ring-faint)" stroke-width="5"/>
    </svg>
    <div class="holder">
      <div class="holder-name">JANE DOE</div>
      <div class="holder-role">Designation</div>
    </div>
    <ul class="contact">
      <li><svg viewBox="0 0 16 16"><path d="M3 1l3 0 1 4-2 1.5c1 2 2.5 3.5 4.5 4.5L11 9l4 1v3c0 1-1 2-2 2C7 15 1 9 1 3c0-1 1-2 2-2z"/></svg>+1234567890</li>
      <li><svg viewBox="0 0 16 16"><path d="M1 3h14v10H1z M1 3l7 6 7-6" fill="none" stroke="#2f3a40" stroke-width="1.8"/></svg>janedoe@mail.com</li>
      <li><svg viewBox="0 0 16 16"><circle cx="8" cy="8" r="6" fill="none" stroke="#2f3a40" stroke-width="1.8"/><path d="M2 8h12M8 2v12" stroke="#2f3a40" stroke-width="1.2"/></svg>www.website.com</li>
      <li class="address"><svg viewBox="0 0 16 16"><path d="M8 1l7 7h-2v7H9v-5H7v5H3V8H1z"/></svg><span>Building No., Street,<br>City, State,<br>ZipCode</span></li>
    </ul>
  </section>
</main>
</body>
</html>
```